How to sell with Quonvel.com

We need an icon/image to describe how sellers can work with us. Here is the typical process a seller can sell with us:
1. A seller register an account and gets verified;
2. Seller publishes his products.
3. A buyer places an order on this seller's product.
4. This seller ships item/product.
5. Buy confirms delivery.
6. We/Quonvel releases funds to the seller.

Please use a single image/icon to describe the above 6-step process.

Reference url: http://www.quonvel.example/seller-center.html

Requirements
Must have
• 1. The above six steps should be in a single icon/image.
• 2. Each step should have each own icon with proper text notation.
• 3. The image/icon created should be 700 px in length.
Nice to have
• The six steps/icons are in different colors, all of which are matching the colors of quonvel.com.

```html
<!DOCTYPE html>
<html lang="en">
<head>
<meta charset="utf-8">
<title>How to sell with Quonvel.com</title>
<link href="https://fonts.googleapis.com/css2?family=Arimo:wght@400&display=swap" rel="stylesheet">
<style>
  :root {
    --brand-blue: #1f86cf;
    --outline-blue: #3a8fd0;
    --label-ink: #1e1e1e;
    --divider-grey: #b8b8b8;
    --form-grey: #d9dde2;
    --canvas-bg: #ffffff;
  }
  html, body {
    margin: 0;
    padding: 0;
    width: 1200px;
    height: 225px;
    overflow: hidden;
    background: var(--canvas-bg);
  }
  .process-strip {
    position: absolute;
    left: 0;
    top: 16px;
    width: 1200px;
    height: 192px;
  }
  .step-label {
    font-family: "Arimo", Arial, sans-serif;
    font-size: 10.6px;
    fill: var(--label-ink);
  }
  .divider {
    stroke: var(--divider-grey);
    stroke-width: 0.8;
    stroke-dasharray: 1.2 1.6;
  }
  .icon-fill { fill: var(--brand-blue); }
  .icon-stroke { fill: none; stroke: var(--brand-blue); stroke-linecap: round; stroke-linejoin: round; }
  .icon-thin { fill: none; stroke: var(--outline-blue); stroke-width: 0.9; stroke-linejoin: round; }
</style>
</head>
<body>
<svg class="process-strip" viewBox="0 0 708 113" preserveAspectRatio="xMidYMid meet" role="img" aria-label="Six steps to sell with Quonvel">
  <!-- connectors -->
  <line class="divider" x1="72" y1="74" x2="130" y2="74"/>
  <line class="divider" x1="188" y1="74" x2="244" y2="74"/>
  <line class="divider" x1="316" y1="74" x2="360" y2="74"/>
  <line class="divider" x1="450" y1="74" x2="505" y2="74"/>
  <line class="divider" x1="570" y1="74" x2="628" y2="74"/>

  <!-- step 1: registration form with tick -->
  <g class="step-register">
    <rect x="12" y="4" width="42" height="50" fill="#f6f8fa" stroke="var(--form-grey)" stroke-width="1"/>
    <rect x="12" y="4" width="42" height="6" class="icon-fill"/>
    <rect x="16" y="15" width="5" height="4" class="icon-fill"/>
    <rect x="24" y="16" width="24" height="2" fill="var(--form-grey)"/>
    <rect x="16" y="24" width="5" height="4" class="icon-fill"/>
    <rect x="24" y="25" width="20" height="2" fill="var(--form-grey)"/>
    <rect x="16" y="33" width="5" height="4" class="icon-fill"/>
    <rect x="24" y="34" width="14" height="2" fill="var(--form-grey)"/>
    <rect x="16" y="42" width="5" height="4" class="icon-fill"/>
    <rect x="24" y="43" width="18" height="2" fill="var(--form-grey)"/>
    <polyline class="icon-stroke" stroke-width="5" points="40,28 50,39 74,12"/>
  </g>

  <!-- step 2: upload -->
  <g class="step-publish">
    <path class="icon-fill" d="M138 36 v18 h40 v-18 h-7 v11 h-26 v-11z"/>
    <polygon class="icon-fill" points="158,8 144,23 152,23 152,42 164,42 164,23 172,23"/>
  </g>

  <!-- step 3: shopping cart with plus -->
  <g class="step-order">
    <polyline class="icon-stroke" stroke-width="2.2" points="244,20 252,20 258,44 286,44"/>
    <polygon class="icon-thin" stroke-width="1.4" points="254,25 292,25 288,40 257,40"/>
    <line class="icon-thin" x1="264" y1="25" x2="265" y2="40"/>
    <line class="icon-thin" x1="273" y1="25" x2="273" y2="40"/>
    <line class="icon-thin" x1="282" y1="25" x2="281" y2="40"/>
    <line class="icon-thin" x1="255" y1="32" x2="290" y2="32"/>
    <circle class="icon-fill" cx="262" cy="50" r="3"/>
    <circle class="icon-fill" cx="284" cy="50" r="3"/>
    <path class="icon-stroke" stroke-width="2" d="M300 6 v10 M295 11 h10"/>
  </g>

  <!-- step 4: airplane -->
  <g class="step-ship" transform="translate(400 30) rotate(-40) scale(1.05)">
    <path class="icon-fill" d="M30,0 C30,-3 26,-4 22,-4 L8,-4 L-8,-26 L-15,-26 L-5,-4 L-20,-4 L-26,-12 L-31,-12 L-27,0 L-31,12 L-26,12 L-20,4 L-5,4 L-15,26 L-8,26 L8,4 L22,4 C26,4 30,3 30,0Z"/>
  </g>

  <!-- step 5: box with tick -->
  <g class="step-delivery">
    <path class="icon-thin" d="M514 30 L536 22 L558 30 L536 38 Z M514 30 V50 L536 58 L558 50 V30 M536 38 V58 M525 26 L547 34 V42"/>
    <path class="icon-thin" d="M514 30 L508 36 L530 44 L536 38 M558 30 L564 36 L542 44 L536 38"/>
    <polyline class="icon-stroke" stroke-width="5" points="526,14 536,24 556,2"/>
  </g>

  <!-- step 6: funds released -->
  <g class="step-funds">
    <circle class="icon-stroke" stroke-width="3" cx="648" cy="34" r="17"/>
    <text x="648" y="43" text-anchor="middle" class="icon-fill" font-family="Arimo, Arial, sans-serif" font-size="24">$</text>
  </g>

  <!-- labels -->
  <text class="step-label" x="10" y="96">Register and</text>
  <text class="step-label" x="10" y="110">get verified</text>
  <text class="step-label" x="138" y="96">Publish</text>
  <text class="step-label" x="138" y="110">products</text>
  <text class="step-label" x="250" y="96">Buyers place</text>
  <text class="step-label" x="250" y="110">orders</text>
  <text class="step-label" x="362" y="96">Sellers ship</text>
  <text class="step-label" x="362" y="110">merchandizes</text>
  <text class="step-label" x="513" y="96">Delivery</text>
  <text class="step-label" x="513" y="110">confirmed</text>
  <text class="step-label" x="630" y="96">Quonvel</text>
  <text class="step-label" x="630" y="110">releases funds</text>
</svg>
</body>
</html>
```